Customs House descriptive business cards

We require a two-sided business card that has a simple yet elegant design. We want to be able to promote our services as a customs house. This card should include our logo, contact info and services offered with the logo being on one side and the contact info and services on the flip side

Target Market(s)

Importers / exporters to and from the Bahamas

Industry/Entity Type

Logistics

Contact Information for Business Card

The front side of the card could have the logo and the flip side should have the other relevant info

Font styles to use
Serif

Colors

Designer to choose colors to be used in the design.

Requirements
Must have
• (Kelpway Brokers Ltd) Logo, address and contact info also services:
• import customs clearance, Delivery & HAndling services,Florida pickups, Export packing & Crating Services, export customs clearance, Consulting

```html
<!DOCTYPE html>
<html lang="en">
<head>
<meta charset="utf-8">
<title>Kelpway Brokers Ltd — Business Card</title>
<link rel="stylesheet" href="https://fonts.googleapis.com/css2?family=Tinos:wght@400;700&family=Lato:wght@400&display=swap">
<style>
  :root {
    --stage: #222222;
    --card-white: #ffffff;
    --brand-blue: #1a8ad0;
    --blue-light: #239bd8;
    --blue-deep: #1c78c3;
    --ink: #222222;
    --rule: #cfe6f5;
    --on-blue: #ffffff;
  }
  * { margin: 0; padding: 0; box-sizing: border-box; }
  html, body { width: 1200px; height: 900px; overflow: hidden; background: var(--stage); }
  .stage { position: relative; width: 1200px; height: 900px; }

  .card {
    position: absolute; top: 200px; width: 310px; height: 502px;
    box-shadow: 3px 4px 6px rgba(0,0,0,0.55);
  }
  .card--details {
    left: 253px; background: var(--card-white);
    border-radius: 62px 0 62px 0;
  }
  .card--brand {
    left: 627px;
    background: radial-gradient(circle at 45% 50%, var(--blue-light) 0%, #2190d0 55%, var(--blue-deep) 100%);
    border-radius: 0 62px 0 62px;
    color: var(--on-blue);
  }

  .brand-name {
    position: absolute; left: 0; width: 100%;
    display: flex; align-items: center; justify-content: center; gap: 10px;
    font-family: "Tinos", serif; font-weight: 700;
  }
  .card--details .brand-name { top: 142px; font-size: 22px; color: var(--brand-blue); }
  .brand-dot { width: 14px; height: 14px; border-radius: 50%; background: currentColor; flex: none; }

  .person { position: absolute; left: 28px; top: 256px; }
  .person__name {
    font-family: "Tinos", serif; font-weight: 700; font-size: 17.5px;
    color: var(--brand-blue); letter-spacing: 0.3px; line-height: 20px;
  }
  .person__role { font-family: "Lato", sans-serif; font-size: 14px; color: var(--ink); line-height: 18px; }

  .contact { position: absolute; left: 26px; top: 299px; list-style: none; }
  .contact li {
    display: flex; align-items: center; gap: 5px;
    font-family: "Lato", sans-serif; font-size: 14.5px; color: var(--ink); line-height: 18.5px;
  }
  .contact svg { width: 11px; height: 11px; fill: var(--brand-blue); flex: none; }

  .divider { position: absolute; left: 29px; top: 362px; width: 232px; height: 1px; background: var(--rule); }

  .services { position: absolute; left: 26px; top: 373px; list-style: none; }
  .services li {
    display: flex; align-items: center; gap: 5px;
    font-family: "Lato", sans-serif; font-size: 14.5px; color: var(--ink); line-height: 18px;
  }
  .services li::before {
    content: ""; width: 8px; height: 8px; border-radius: 50%; background: var(--brand-blue); flex: none;
  }

  .card--brand .brand-name { top: 268px; font-size: 30px; font-weight: 400; letter-spacing: 0.5px; }

  .address {
    position: absolute; left: 0; width: 100%; top: 431px; text-align: center;
    font-family: "Lato", sans-serif; font-size: 14.5px; line-height: 18px;
  }
</style>
</head>
<body>
<main class="stage">
  <section class="card card--details" aria-label="Card back: contact and services">
    <div class="brand-name"><span class="brand-dot"></span>Kelpway Brokers Ltd</div>

    <div class="person">
      <p class="person__name">DANIEL ARCHER</p>
      <p class="person__role">Managing Director</p>
    </div>

    <ul class="contact">
      <li><svg viewBox="0 0 12 12" aria-hidden="true"><path d="M1 4c0-1.5 2-2.5 5-2.5S11 2.5 11 4v1H8.5V3.8h-5V5H1z M2.5 6h7l1 4.5h-9z"/></svg>044-555 018 274</li>
      <li><svg viewBox="0 0 12 12" aria-hidden="true"><path d="M1 2.5h10v7H1z M1.6 3.1 6 6.4l4.4-3.3" stroke="#fff" stroke-width="0.9"/></svg>info@kelpwaybrokers.com</li>
      <li><svg viewBox="0 0 12 12" aria-hidden="true"><circle cx="6" cy="6" r="5"/><path d="M3 4.5c1 0 1.5.8 1.3 1.8L5.5 8 4.6 10M7 2c0 1 1 1.3 1.8 1.1L9.8 5" stroke="#fff" stroke-width="0.8" fill="none"/></svg>www.kelpwaybrokers.com</li>
    </ul>

    <div class="divider"></div>

    <ul class="services">
      <li>Import customs clearance</li>
      <li>Delivery &amp; HAndling services</li>
      <li>Florida pickups</li>
      <li>Export packing &amp; Crating Services</li>
      <li>Export customs clearance, Consulting</li>
    </ul>
  </section>

  <section class="card card--brand" aria-label="Card front: brand and address">
    <div class="brand-name">Kelpway Brokers Ltd.</div>
    <p class="address">12345, Address Goes Here<br>Country Name, 123456</p>
  </section>
</main>
</body>
</html>
```